Business Card Design

A card that's appealing to realtors and home buyers..
Something that's memorable,attractive, yet simple.

Business

Home Inspection business.
Name of co. Birchline Home Inspections
Serving Kern, Los Angeles, Santa Barbara & Ventura counties
NBPI Certified Inspectors (Use NBPI certified logo)
http://nbpiguild.example/logos/newlogos/NBPI_Logo008.gif
Carl Movrey
661 555-0142
Owen Movrey
805 555-0187
Email :birchlineinspections@mailvero.example
Also use slogan: Providing peace of mind

```html
<!DOCTYPE html>
<html lang="en">
<head>
<meta charset="utf-8">
<title>Birchline Home Inspections – Business Card</title>
<link rel="stylesheet" href="https://fonts.googleapis.com/css2?family=Oswald:wght@500;600&family=Open+Sans:wght@400;600&display=swap">
<style>
  :root {
    --stage: #e9ebee;
    --card: #ffffff;
    --ink: #1f2a36;
    --muted: #5d6670;
    --blue: #1a8fd6;
    --blue-deep: #0b4f93;
    --blue-light: #4fc3f2;
    --badge: #c9d3dd;
  }
  * { box-sizing: border-box; margin: 0; padding: 0; }
  html, body { width: 1200px; height: 864px; overflow: hidden; }
  body {
    background: var(--stage);
    font-family: "Open Sans", sans-serif;
    display: flex; flex-direction: column; align-items: center; justify-content: center;
    gap: 24px;
  }
  .card {
    position: relative;
    width: 700px; height: 400px;
    background: var(--card);
    box-shadow: 0 6px 20px rgba(0,0,0,.12);
    overflow: hidden;
  }
  .brand { display: flex; align-items: center; gap: 16px; white-space: nowrap; }
  .brand-mark {
    width: 74px; height: 74px; border-radius: 50%;
    border: 9px solid var(--blue);
    flex: none;
  }
  .brand-name {
    font-family: "Oswald", sans-serif; font-weight: 600;
    color: var(--blue-deep);
    text-transform: uppercase; letter-spacing: 3px;
    font-size: 28px; line-height: 1.15;
  }

  /* front */
  .front-stack {
    position: absolute; left: 50%; top: 50%; transform: translate(-50%, -58%);
    display: flex; flex-direction: column; align-items: center; gap: 16px;
  }
  .slogan {
    font-size: 14px; color: var(--muted); font-style: normal; letter-spacing: 2px;
    text-transform: uppercase;
  }
  .certification {
    position: absolute; left: 50%; bottom: 34px; transform: translateX(-50%);
    display: flex; align-items: center; gap: 10px; white-space: nowrap;
    font-size: 12px; font-weight: 600; color: var(--blue-deep); letter-spacing: 1px;
    text-transform: uppercase;
  }
  .certification-badge {
    width: 28px; height: 28px; border-radius: 50%; background: var(--badge); flex: none;
  }

  /* back */
  .card-back .brand { position: absolute; right: 56px; top: 52px; }
  .card-back .brand-mark { width: 62px; height: 62px; border-width: 8px; }
  .card-back .brand-name { font-size: 23px; }
  .person { position: absolute; left: 48px; top: 140px; }
  .person-name {
    font-family: "Oswald", sans-serif; font-weight: 500;
    font-size: 26px; color: var(--blue); text-transform: uppercase; letter-spacing: 1px;
  }
  .person-role { font-size: 12px; color: var(--muted); letter-spacing: 2px; text-transform: uppercase; }
  .contacts { position: absolute; left: 48px; top: 220px; list-style: none; }
  .contacts li {
    display: flex; align-items: center; gap: 10px; white-space: nowrap;
    font-size: 12px; color: var(--ink); margin-bottom: 9px;
  }
  .contacts svg { width: 14px; height: 14px; fill: var(--blue-deep); flex: none; }
  .contact-label { color: var(--muted); }
  .band { position: absolute; left: 0; bottom: 0; width: 700px; height: 150px; }
  .service-area {
    position: absolute; right: 36px; bottom: 30px; width: 280px;
    text-align: right; color: #fff; font-size: 13px; font-weight: 600;
    line-height: 1.45; letter-spacing: .3px;
  }
</style>
</head>
<body>

<section class="card card-front">
  <div class="front-stack">
    <div class="brand">
      <span class="brand-mark"></span>
      <span class="brand-name">Birchline<br>Home Inspections</span>
    </div>
    <p class="slogan">Providing peace of mind</p>
  </div>
  <p class="certification"><span class="certification-badge"></span>NBPI Certified Inspectors</p>
</section>

<section class="card card-back">
  <div class="brand">
    <span class="brand-mark"></span>
    <span class="brand-name">Birchline<br>Home Inspections</span>
  </div>

  <div class="person">
    <p class="person-name">Carl Movrey</p>
    <p class="person-role">General Manager</p>
  </div>

  <ul class="contacts">
    <li><svg viewBox="0 0 24 24"><path d="M6.6 10.8a15 15 0 0 0 6.6 6.6l2.2-2.2c.3-.3.7-.4 1-.2 1.1.4 2.3.6 3.6.6.6 0 1 .4 1 1V20c0 .6-.4 1-1 1A17 17 0 0 1 3 4c0-.6.4-1 1-1h3.5c.6 0 1 .4 1 1 0 1.3.2 2.5.6 3.6.1.3 0 .7-.2 1z"/></svg>661 555-0142</li>
    <li><svg viewBox="0 0 24 24"><path d="M7 1h10a2 2 0 0 1 2 2v18a2 2 0 0 1-2 2H7a2 2 0 0 1-2-2V3a2 2 0 0 1 2-2zm0 3v14h10V4zm5 15.5a1 1 0 1 0 0 2 1 1 0 0 0 0-2z"/></svg><span class="contact-label">Owen Movrey</span>805 555-0187</li>
    <li><svg viewBox="0 0 24 24"><path d="M2 5h20v14H2zm2 2v.5l8 5 8-5V7zm0 2.8V17h16V9.8l-8 5z"/></svg>birchlineinspections@mailvero.example</li>
    <li><svg viewBox="0 0 24 24"><path d="M12 2a10 10 0 1 0 0 20 10 10 0 0 0 0-20zm0 2a8 8 0 0 1 7.7 6H4.3A8 8 0 0 1 12 4zm-7.7 8h15.4a8 8 0 0 1-15.4 0z"/></svg>www.birchlinehome.example</li>
  </ul>

  <svg class="band" viewBox="0 0 700 150" preserveAspectRatio="none" aria-hidden="true">
    <defs>
      <linearGradient id="bandFill" x1="0" y1="0" x2="1" y2="1">
        <stop offset="0" stop-color="#1a8fd6"/>
        <stop offset="1" stop-color="#0b4f93"/>
      </linearGradient>
    </defs>
    <path d="M0 128 L300 128 C330 128 330 50 370 50 L700 50 L700 150 L0 150 Z" fill="var(--blue-light)"/>
    <path d="M0 136 L305 136 C335 136 335 60 378 60 L700 60 L700 150 L0 150 Z" fill="url(#bandFill)"/>
  </svg>
  <p class="service-area">Serving Kern, Los Angeles,<br>Santa Barbara &amp; Ventura counties</p>
</section>

</body>
</html>
```